New custom software business needs a Wordpress site

We need a Wordpress site for a new company based out of Chicago called 'Vellora Consulting'. Using a mix of on and off-shore resources we build custom software solutions, mainly focusing on small to medium sized companies. We help our customers "aspire" to do great things.
We have a basic site up here: https://brindlewave.example/. We worked on the content for it but not the branding. For now, this houses all the pages (except for a Contact Us page we'll be adding soon) for the foreseeable future.
We also have a new logo (attached) that we'd like to base the styling/colors on.
Target Market(s)
Small to medium sized companies that require tech resources
Industry/Entity Type
Software
Nice to have
- Teamwork, tech, professional but not elitist

```html
<!DOCTYPE html>
<html lang="en">
<head>
<meta charset="utf-8">
<title>Vellora Consulting</title>
<link href="https://fonts.googleapis.com/css2?family=Poppins:wght@400;500;600;700&family=Lato:wght@400;700&display=swap" rel="stylesheet">
<style>
:root{
  --blue:#0a54b4;
  --blue-deep:#0d4a9e;
  --navy:#163a6b;
  --footer:#0f2748;
  --ink:#1f2a38;
  --text:#3b4350;
  --mist:#cbdde5;
  --line:#e3e8ee;
  --white:#ffffff;
}
*{box-sizing:border-box;margin:0;padding:0}
html,body{width:1200px;height:3383px;overflow:hidden}
body{position:relative;background:var(--white);font-family:"Lato",sans-serif;color:var(--text)}
.abs{position:absolute}
.heading-font{font-family:"Poppins",sans-serif}

/* header */
.site-header{position:absolute;left:0;top:0;width:1200px;height:125px;display:flex;align-items:center;justify-content:center;gap:12px}
.brand-mark{width:34px;height:34px;background:var(--blue);border-radius:50%}
.brand-name{font-family:"Poppins",sans-serif;font-weight:600;font-size:30px;color:var(--blue);letter-spacing:1px}
.main-nav{position:absolute;left:0;top:125px;width:1200px;height:70px;background:var(--blue);display:flex;align-items:center;justify-content:center;font-family:"Poppins",sans-serif;font-size:18px;color:var(--white)}
.main-nav span{margin:0 22px}

/* hero */
.hero-photo{position:absolute;left:0;top:195px;width:1200px;height:689px;background:linear-gradient(120deg,#e9e6ee 0%,#c9ccd8 25%,#1d3f73 45%,#0d2446 70%,#2a4160 100%)}
.hero-card{position:absolute;left:0;top:310px;width:542px;height:445px;background:var(--blue-deep);border-radius:0 22px 22px 0;padding:40px 0 0 82px;color:var(--white)}
.hero-kicker{font-family:"Poppins",sans-serif;font-weight:600;font-size:27px}
.hero-title{font-family:"Poppins",sans-serif;font-weight:700;font-size:57px;line-height:66px;margin-top:8px}
.hero-text{font-family:"Poppins",sans-serif;font-size:19px;line-height:33px;margin-top:18px;width:420px}
.btn{display:inline-block;font-family:"Poppins",sans-serif;font-weight:500;font-size:15px;border-radius:24px;padding:0 22px;height:48px;line-height:48px}
.btn-light{background:var(--white);color:var(--blue);margin-top:26px}
.btn-blue{background:var(--blue);color:var(--white)}

/* shared */
.section-bar{width:60px;height:4px;background:var(--blue)}
.section-title{font-family:"Poppins",sans-serif;font-weight:400;font-size:34px;color:var(--ink)}
.body-copy{font-size:15px;line-height:30px;text-align:justify;color:var(--text)}
.photo-frame{border:1.5px solid var(--navy)}
.photo-tab{background:#eceef1;border:1.5px solid var(--navy)}

/* services */
.service{position:absolute;top:1578px;height:352px;width:600px;color:var(--white)}
.service-left{left:0;background:var(--navy)}
.service-right{left:600px;background:var(--blue)}
.service-title{position:absolute;top:75px;font-family:"Lato",sans-serif;font-weight:700;font-size:27px;display:flex;align-items:center;gap:14px}
.service-title i{display:block;width:55px;height:2px;background:var(--white)}
.service-copy{position:absolute;top:125px;font-size:15px;line-height:30px;text-align:justify;width:430px}
.service-arrow{position:absolute;top:307px;right:38px}

/* contact */
.contact-photo{position:absolute;left:0;top:2572px;width:541px;height:498px;background:linear-gradient(135deg,#25466f,#0f2a4d 55%,#3b6a9e)}
.contact-panel{position:absolute;left:541px;top:2572px;width:652px;height:498px;background:var(--mist)}
.field{position:absolute;height:52px;background:var(--white);font-size:16px;color:#555;padding-left:19px;line-height:52px}

/* footer */
.site-footer{position:absolute;left:0;top:3070px;width:1200px;height:313px;background:var(--footer);color:var(--white);font-family:"Poppins",sans-serif}
.footer-col{position:absolute;top:57px}
.footer-col h4{font-weight:600;font-size:17px;letter-spacing:.5px;margin-bottom:14px}
.footer-col li{list-style:none;font-size:15px;line-height:30px;display:flex;align-items:center;gap:12px}
.chev{color:#9fb6d4;font-size:14px}
.social{display:flex;gap:10px}
.social span{width:36px;height:36px;border:1.5px solid var(--white);border-radius:50%}
.copyright{position:absolute;left:107px;top:261px;width:977px;border-top:1px solid #3a5476;text-align:center;padding-top:14px;font-size:15px}
</style>
</head>
<body>

<header class="site-header">
  <span class="brand-mark"></span>
  <span class="brand-name">VELLORA CONSULTING</span>
</header>
<nav class="main-nav">
  <span>Home</span><span>I</span><span>Services</span><span>I</span><span>Why Vellora?</span><span>I</span><span>Vellora Leadership</span>
</nav>

<section>
  <div class="hero-photo" role="img" aria-label="Hands holding a smartphone surrounded by glowing AI technology icons over a laptop"></div>
  <div class="hero-card">
    <div class="hero-kicker">WELCOME TO</div>
    <div class="hero-title">VELLORA<br>CONSULTING</div>
    <p class="hero-text">Welcome to Vellora, a software consulting company specializing in serving small to medium size businesses.</p>
    <span class="btn btn-light">LEARN MORE</span>
  </div>
</section>

<section class="about">
  <div class="abs photo-tab" style="left:437px;top:968px;width:71px;height:69px"></div>
  <div class="abs photo-frame" style="left:57px;top:1000px;width:437px;height:417px"></div>
  <div class="abs" role="img" aria-label="Woman working on a tablet in an industrial office" style="left:37px;top:982px;width:437px;height:414px;background:linear-gradient(135deg,#5b6f86,#a9b6c3 50%,#3d5168)"></div>
  <div class="abs section-bar" style="left:545px;top:967px"></div>
  <h2 class="abs section-title" style="left:545px;top:984px">ABOUT VELLORA CONSULTING</h2>
  <p class="abs" style="left:545px;top:1038px;width:570px;font-size:23px;line-height:35px;color:var(--ink)">Welcome to Vellora, a software consulting company specializing in serving small to medium size businesses.</p>
  <p class="abs body-copy" style="left:545px;top:1123px;width:565px">We understand the unique challenges and opportunities that these companies face, and we are dedicated to helping them succeed through innovative technology solutions.</p>
  <p class="abs body-copy" style="left:545px;top:1222px;width:565px">Our team of experienced professionals has a diverse range of skills and expertise, making us well-equipped to handle any project, big or small. We specialize in custom software development, working closely with our clients to understand their specific needs and build solutions that meet their requirements.</p>
  <span class="abs btn btn-blue" style="left:540px;top:1368px">LEARN MORE</span>
</section>

<div class="abs section-bar" style="left:568px;top:1482px"></div>
<h2 class="abs section-title" style="left:0;width:1200px;text-align:center;top:1500px">OUR SERVICES</h2>

<section class="service service-left">
  <svg class="abs" style="left:64px;top:30px" width="54" height="66" viewBox="0 0 54 66" fill="none" stroke="#fff" stroke-width="3">
    <circle cx="27" cy="26" r="12"/><path d="M21 38v8h12v-8"/><circle cx="27" cy="55" r="8"/>
    <path d="M27 4v5M10 10l4 4M44 10l-4 4"/>
  </svg>
  <div class="service-title" style="left:147px">Custom Solution Delivery <i></i></div>
  <p class="service-copy" style="left:81px">Vellora offers a range of services focused on helping businesses and organizations deliver software solutions to their customers or users. This can include a wide variety of activities, such as designing and developing custom software, implementing and integrating software solutions, and providing ongoing maintenance and support for software systems.</p>
  <svg class="service-arrow" width="24" height="24" viewBox="0 0 24 24"><circle cx="12" cy="12" r="11" fill="#fff"/><path d="M7 12h9M12 8l4 4-4 4" stroke="#163a6b" stroke-width="2" fill="none"/></svg>
</section>
<section class="service service-right">
  <svg class="abs" style="left:48px;top:34px" width="84" height="84" viewBox="0 0 84 84" fill="none" stroke="#fff" stroke-width="3">
    <circle cx="42" cy="42" r="38"/><circle cx="42" cy="34" r="7"/><circle cx="26" cy="40" r="5"/><circle cx="58" cy="40" r="5"/>
    <path d="M30 60c0-10 24-10 24 0M16 58c0-8 14-8 14-6M68 58c0-8-14-8-14-6"/>
  </svg>
  <div class="service-title" style="left:148px">Staff Augmentation <i></i></div>
  <p class="service-copy" style="left:80px">Let Vellora help you supplement your existing software development teams with additional resources and expertise. We provided access to experienced software developers who can work with your in-house teams to help them deliver software projects on time and within budget.</p>
  <svg class="service-arrow" width="24" height="24" viewBox="0 0 24 24"><circle cx="12" cy="12" r="11" fill="#fff"/><path d="M7 12h9M12 8l4 4-4 4" stroke="#0a54b4" stroke-width="2" fill="none"/></svg>
</section>

<section class="why">
  <div class="abs section-bar" style="left:83px;top:2045px"></div>
  <h2 class="abs section-title" style="left:83px;top:2062px">WHY VELLORA?</h2>
  <p class="abs body-copy" style="left:88px;top:2120px;width:543px">At Vellora, we are proud to have a team of seasoned IT professionals who understand what it takes to deliver a quality solution. Our team members have a wealth of experience and expertise in a variety of different areas, including software development, system integration, data migration, and software maintenance and support.</p>
  <p class="abs body-copy" style="left:88px;top:2290px;width:543px">We understand that delivering a high-quality software solution requires more than just technical expertise. It also requires a deep understanding of the needs and challenges of our clients, and the ability to work closely with them to develop a solution that meets their specific requirements.</p>
  <span class="abs btn btn-blue" style="left:77px;top:2437px">LEARN MORE</span>
  <div class="abs photo-frame" style="left:690px;top:2027px;width:437px;height:412px"></div>
  <div class="abs photo-tab" style="left:674px;top:2405px;width:71px;height:69px"></div>
  <div class="abs" role="img" aria-label="Smiling business team standing together in an office" style="left:709px;top:2044px;width:437px;height:415px;background:linear-gradient(135deg,#c6c9ce,#7b8796 45%,#3f4b5c)"></div>
</section>

<section>
  <div class="contact-photo" role="img" aria-label="Software developer coding at a desk with multiple monitors"></div>
  <div class="contact-panel"></div>
  <div class="abs section-bar" style="left:599px;top:2611px"></div>
  <h2 class="abs section-title" style="left:599px;top:2628px">GET IN TOUCH</h2>
  <div class="field" style="left:599px;top:2697px;width:250px">Firtst Name</div>
  <div class="field" style="left:862px;top:2697px;width:250px">Last Name</div>
  <div class="field" style="left:599px;top:2762px;width:513px">Email ID</div>
  <div class="field" style="left:599px;top:2832px;width:250px">Company</div>
  <div class="field" style="left:862px;top:2832px;width:250px">Enquiry</div>
  <div class="field" style="left:599px;top:2898px;width:513px">Message</div>
  <span class="abs btn btn-blue" style="left:599px;top:2981px;padding:0 26px">SUBMIT NOW</span>
</section>

<footer class="site-footer">
  <div class="abs" style="left:140px;top:80px;width:140px;text-align:center">
    <span style="display:inline-block;width:40px;height:40px;border-radius:50%;background:#2f6fc4"></span>
    <div style="font-weight:500;font-size:18px;letter-spacing:1px;margin-top:8px">VELLORA</div>
    <div style="font-size:10px;letter-spacing:2px;color:#9fb6d4">CONSULTING</div>
  </div>
  <div class="abs social" style="left:129px;top:198px"><span></span><span></span><span></span><span></span></div>
  <div class="footer-col" style="left:381px">
    <h4>QUICK LINKS</h4>
    <ul><li><span class="chev">»</span>Home</li><li><span class="chev">»</span>Services</li><li><span class="chev">»</span>Why Vellora?</li><li><span class="chev">»</span>Vellora Leadership</li></ul>
  </div>
  <div class="footer-col" style="left:603px">
    <h4>CONTACT</h4>
    <ul>
      <li style="align-items:flex-start"><svg width="18" height="22" viewBox="0 0 18 22"><path d="M9 1a7 7 0 0 0-7 7c0 5 7 13 7 13s7-8 7-13a7 7 0 0 0-7-7z" fill="#5b8fd6"/><circle cx="9" cy="8" r="2.5" fill="#0f2748"/></svg><span style="margin-left:6px">Dummy,Address here<br>City, Pincode 000 000</span></li>
      <li style="margin-top:10px"><svg width="18" height="18" viewBox="0 0 18 18"><path d="M4 2l3 3-2 2c1 2 3 4 5 5l2-2 3 3-2 3C7 15 3 11 2 4z" fill="#5b8fd6"/></svg><span style="margin-left:6px">+1-555-014-2270</span></li>
      <li style="margin-top:14px"><svg width="18" height="14" viewBox="0 0 18 14"><rect width="18" height="14" rx="1" fill="#5b8fd6"/><path d="M1 1l8 6 8-6" stroke="#0f2748" stroke-width="1.5" fill="none"/></svg><span style="margin-left:6px">info@vellora.example</span></li>
    </ul>
  </div>
  <div class="footer-col" style="left:870px">
    <h4>OTHER LINKS</h4>
    <ul><li><span class="chev">»</span>Tearms &amp; Condition</li><li><span class="chev">»</span>Privacy Policy</li><li><span class="chev">»</span>Personal Data &amp; Cookies</li><li><span class="chev">»</span>Contact</li></ul>
  </div>
  <div class="copyright">2022 Vellora Consulting. All Rights Reserved.</div>
</footer>

</body>
</html>
```